Letterhead & Greeting Card Design Project

I need a few files prepared for dynamic digital printing: letterhead and 2 postcards with an envelope for each. Enclosed are specific directions from the printer for each file and overall. I have also enclosed mockups of what I would like on those designs and some raw files to work with.

Industry/Entity Type

Digital

```html
<!DOCTYPE html>
<html lang="en">
<head>
<meta charset="utf-8">
<title>Cadence Media Letterhead</title>
<link rel="stylesheet" href="https://fonts.googleapis.com/css2?family=Exo+2:wght@600&display=swap">
<style>
  :root {
    --paper: #ffffff;
    --ink: #1a1a1a;
    --brand-grey: #6d6e70;
    --brand-blue: #1e9bd7;
    --cyan: #00aeef;
    --magenta: #ec008c;
    --yellow: #fff200;
    --blue: #2e3192;
    --red: #ed1c24;
    --green: #00a651;
    --dark: #3a3a3a;
    --black: #231f20;
  }
  * { margin: 0; padding: 0; box-sizing: border-box; }
  html, body { width: 949px; height: 1200px; overflow: hidden; background: var(--paper); }
  .sheet { position: relative; width: 949px; height: 1200px; background: var(--paper); }

  .trim-frame {
    position: absolute; left: 46px; top: 46px; width: 854px; height: 1120px;
    border: 2px solid var(--ink);
  }

  .brand {
    position: absolute; right: 93px; top: 92px; height: 60px;
    display: flex; align-items: center; gap: 14px;
  }
  .brand-dot { width: 28px; height: 28px; border-radius: 50%; background: var(--brand-blue); flex: none; }
  .brand-name {
    font-family: "Exo 2", sans-serif; font-weight: 600; font-size: 40px;
    color: var(--brand-grey); letter-spacing: 0.5px; white-space: nowrap; line-height: 1;
  }

  .corner-decoration {
    position: absolute; left: 48px; top: 955px; width: 182px; height: 209px;
    border-top-right-radius: 140px 150px;
    background: linear-gradient(135deg, var(--brand-grey) 0%, var(--brand-grey) 38%, var(--brand-blue) 62%, var(--brand-blue) 100%);
  }

  .reg-mark { position: absolute; width: 26px; height: 26px; }

  .colour-bar { position: absolute; top: 516px; width: 21px; display: flex; flex-direction: column; }
  .colour-bar--left { left: 8px; }
  .colour-bar--right { left: 918px; }
  .swatch { width: 21px; height: 21px; }

  .tone-ramp { position: absolute; left: 369px; top: 1170px; display: flex; }
  .tone-ramp span { width: 19px; height: 20px; }
</style>
</head>
<body>
<div class="sheet">
  <svg width="0" height="0" style="position:absolute">
    <defs>
      <symbol id="registration" viewBox="0 0 26 26">
        <circle cx="13" cy="13" r="8" fill="none" stroke="#1a1a1a" stroke-width="1.2"/>
        <line x1="0" y1="13" x2="26" y2="13" stroke="#1a1a1a" stroke-width="1"/>
        <line x1="13" y1="0" x2="13" y2="26" stroke="#1a1a1a" stroke-width="1"/>
        <circle cx="13" cy="13" r="4" fill="#1a1a1a"/>
      </symbol>
      <symbol id="registration-solid" viewBox="0 0 26 26">
        <circle cx="13" cy="13" r="11" fill="#1a1a1a"/>
        <line x1="0" y1="13" x2="26" y2="13" stroke="#888" stroke-width="1"/>
        <line x1="13" y1="0" x2="13" y2="26" stroke="#888" stroke-width="1"/>
      </symbol>
    </defs>
  </svg>

  <div class="trim-frame"></div>

  <div class="brand">
    <span class="brand-dot"></span>
    <span class="brand-name">Cadence Media</span>
  </div>

  <div class="corner-decoration" role="img" aria-label="Brand ornament area in grey and blue"></div>

  <svg class="reg-mark" style="left:51px;top:7px"><use href="#registration"/></svg>
  <svg class="reg-mark" style="left:864px;top:7px"><use href="#registration"/></svg>
  <svg class="reg-mark" style="left:7px;top:51px"><use href="#registration"/></svg>
  <svg class="reg-mark" style="left:917px;top:51px"><use href="#registration"/></svg>
  <svg class="reg-mark" style="left:7px;top:1114px"><use href="#registration"/></svg>
  <svg class="reg-mark" style="left:917px;top:1114px"><use href="#registration"/></svg>
  <svg class="reg-mark" style="left:51px;top:1165px"><use href="#registration"/></svg>
  <svg class="reg-mark" style="left:864px;top:1165px"><use href="#registration-solid"/></svg>

  <div class="colour-bar colour-bar--left">
    <span class="swatch" style="background:var(--cyan)"></span>
    <span class="swatch" style="background:var(--magenta)"></span>
    <span class="swatch" style="background:var(--yellow)"></span>
    <span class="swatch" style="background:var(--blue)"></span>
    <span class="swatch" style="background:var(--red)"></span>
    <span class="swatch" style="background:var(--green)"></span>
    <span class="swatch" style="background:var(--dark)"></span>
    <span class="swatch" style="background:var(--black)"></span>
  </div>
  <div class="colour-bar colour-bar--right">
    <span class="swatch" style="background:var(--cyan)"></span>
    <span class="swatch" style="background:var(--magenta)"></span>
    <span class="swatch" style="background:var(--yellow)"></span>
    <span class="swatch" style="background:var(--blue)"></span>
    <span class="swatch" style="background:var(--red)"></span>
    <span class="swatch" style="background:var(--green)"></span>
    <span class="swatch" style="background:var(--dark)"></span>
    <span class="swatch" style="background:var(--black)"></span>
  </div>

  <div class="tone-ramp">
    <span style="background:#000"></span>
    <span style="background:#1c1c1c"></span>
    <span style="background:#333"></span>
    <span style="background:#4a4a4a"></span>
    <span style="background:#616161"></span>
    <span style="background:#787878"></span>
    <span style="background:#8f8f8f"></span>
    <span style="background:#a6a6a6"></span>
    <span style="background:#bdbdbd"></span>
    <span style="background:#d4d4d4"></span>
    <span style="background:#ebebeb"></span>
  </div>
</div>
</body>
</html>
```